Pelton Mortgage Capital Business Card

We need a business card design for our mortgage servicing company. In addition to servicing the loans of homeowners, we help homeowners with purchasing their homes and any mortgage refinancing. We would like to see designs that use the colors in the logo attached below (gold-ish yellow and navy blue), and any other design you deem fit! The design should communicate a simpler life with smart mortgages provided by Pelton.

```html
<!DOCTYPE html>
<html lang="en">
<head>
<meta charset="utf-8">
<title>Pelton Mortgage Capital – Business Card</title>
<link href="https://fonts.googleapis.com/css2?family=Abril+Fatface&family=Poppins:wght@400;500;600&display=swap" rel="stylesheet">
<style>
  :root {
    --navy: #25205a;
    --navy-deep: #1d1848;
    --navy-light: #3a2f8a;
    --gold: #e8b23a;
    --gold-soft: #f0cf7f;
    --paper: #ffffff;
    --backdrop: #c9c9c9;
  }
  * { margin: 0; padding: 0; box-sizing: border-box; }
  html, body { width: 1200px; height: 800px; overflow: hidden; }
  body {
    background: var(--backdrop);
    font-family: "Poppins", sans-serif;
    position: relative;
  }
  .card {
    position: absolute;
    top: 245px;
    width: 525px;
    height: 310px;
    border-radius: 22px;
    overflow: hidden;
    box-shadow: 0 14px 30px rgba(0,0,0,0.22);
  }
  /* Front */
  .card-front { left: 50px; background: var(--paper); }
  .front-brand {
    position: absolute;
    left: 0; top: 0;
    width: 262px; height: 310px;
    display: flex; align-items: center; justify-content: center;
  }
  .brand-name {
    font-family: "Poppins", sans-serif;
    font-weight: 600;
    font-size: 30px;
    color: var(--navy);
    line-height: 1.1;
    text-align: center;
  }
  .divider {
    position: absolute;
    left: 262px; top: 40px;
    width: 1.5px; height: 230px;
    background: linear-gradient(to bottom, rgba(232,178,58,0), var(--gold) 30%, var(--gold) 70%, rgba(232,178,58,0));
  }
  .front-details {
    position: absolute;
    left: 288px; top: 56px;
    color: var(--navy);
  }
  .person-name {
    font-family: "Abril Fatface", serif;
    font-size: 25px;
    color: var(--gold);
    letter-spacing: 0.5px;
    line-height: 1;
  }
  .person-title {
    font-size: 11px;
    letter-spacing: 0.6px;
    text-transform: uppercase;
    margin-top: 4px;
  }
  .contact-list { list-style: none; margin-top: 16px; }
  .contact-list li {
    display: flex; align-items: center; gap: 8px;
    font-size: 13px; line-height: 1.55;
  }
  .contact-icon { width: 12px; height: 12px; flex: none; }
  .web-accent { color: var(--gold); }
  .address {
    font-size: 13px; line-height: 1.4;
    margin-top: 10px;
  }
  /* Back */
  .card-back { left: 625px; }
  .back-pattern {
    position: absolute; inset: 0;
    background: radial-gradient(ellipse at 70% 40%, var(--navy-light) 0%, var(--navy) 45%, var(--navy-deep) 100%);
  }
  .back-brand {
    position: absolute; inset: 0;
    display: flex; align-items: center; justify-content: center;
  }
  .back-brand .brand-name { color: var(--gold); }
</style>
</head>
<body>
  <section class="card card-front" aria-label="Business card front">
    <div class="front-brand">
      <p class="brand-name">Pelton Mortgage</p>
    </div>
    <div class="divider"></div>
    <div class="front-details">
      <h1 class="person-name">Elliot Marsh</h1>
      <p class="person-title">Managing Director</p>
      <ul class="contact-list">
        <li>
          <svg class="contact-icon" viewBox="0 0 24 24"><path fill="#e8b23a" d="M6.6 10.8a15.1 15.1 0 0 0 6.6 6.6l2.2-2.2a1 1 0 0 1 1-.25 11.4 11.4 0 0 0 3.6.57 1 1 0 0 1 1 1V20a1 1 0 0 1-1 1A17 17 0 0 1 3 4a1 1 0 0 1 1-1h3.5a1 1 0 0 1 1 1c0 1.25.2 2.45.57 3.57a1 1 0 0 1-.25 1z"/></svg>
          044-987 210 365
        </li>
        <li>
          <svg class="contact-icon" viewBox="0 0 24 24"><rect x="2" y="5" width="20" height="14" rx="1.5" fill="#e8b23a"/><path d="M2.5 6 12 13l9.5-7" stroke="#fff" stroke-width="1.6" fill="none"/></svg>
          hello@peltonmail.com
        </li>
        <li>
          <svg class="contact-icon" viewBox="0 0 24 24"><circle cx="12" cy="12" r="10" fill="#e8b23a"/><path d="M2 12h20M12 2c3 3 3 17 0 20M12 2c-3 3-3 17 0 20" stroke="#fff" stroke-width="1.4" fill="none"/></svg>
          <span>www.<span class="web-accent">peltonhomes</span>.com</span>
        </li>
      </ul>
      <p class="address">118, Harbour View Road<br>30917, Lakeside State</p>
    </div>
  </section>

  <section class="card card-back" aria-label="Business card back">
    <div class="back-pattern" role="img" aria-label="Subtle embossed repeating brand pattern on navy"></div>
    <div class="back-brand">
      <p class="brand-name">Pelton Mortgage</p>
    </div>
  </section>
</body>
</html>
```